Logo + Business Card design for a new start-up

For a new start-up company, a global brand expansion agency (marketing, brand consulting solutions) we're looking for a creative designer to help us design both the company logo and business card for project managers.

The name of the company is 'Harwick Crest Partners' (abbreviated: HCP, website: harwickcrestpartners.example)

The logo design should give the company an image of "corporate" (serious), but not too plain/simple. Playing with overlapping fonts, or font colors is an option. Logo with only the abbreviation HCP is also an option.

The business cards need to have a touch of creativity to them, any style/colors can be used, and should underline the nature of business.

Industry/Entity Type

Business

```html
<!DOCTYPE html>
<html lang="en">
<head>
<meta charset="utf-8">
<title>Harwick Crest Partners – Business Card</title>
<link rel="stylesheet" href="https://fonts.googleapis.com/css2?family=Open+Sans:ital,wght@0,400;0,600;0,700;1,400&display=swap">
<style>
  :root {
    --backdrop: #e9e6e2;
    --card: #231f20;
    --accent-red: #e8202a;
    --accent-blue: #1177c3;
    --text-light: #f4f4f4;
    --text-muted: #d8d8d8;
  }
  * { box-sizing: border-box; margin: 0; padding: 0; }
  html, body {
    width: 1200px; height: 891px; overflow: hidden;
    background: var(--backdrop);
    font-family: "Open Sans", Arial, sans-serif;
  }
  .canvas {
    position: relative; width: 1200px; height: 891px;
    display: flex; align-items: center; justify-content: center; gap: 60px;
  }
  .card {
    position: relative; width: 520px; height: 298px;
    background: var(--card);
    box-shadow: 0 10px 28px rgba(0,0,0,.25);
    overflow: hidden;
  }
  .edge-tab {
    position: absolute; width: 12px; height: 74px; border-radius: 6px;
  }
  .edge-tab--blue { background: var(--accent-blue); left: -6px; top: 38px; }
  .edge-tab--red { background: var(--accent-red); right: -6px; bottom: 38px; }

  .wordmark {
    color: var(--accent-red);
    font-weight: 400;
    letter-spacing: .5px;
    display: flex; align-items: center; gap: 12px;
  }
  .wordmark__dot {
    width: 14px; height: 14px; border-radius: 50%;
    background: var(--accent-blue); flex: none;
  }
  .card--front .wordmark {
    position: absolute; left: 0; right: 0; top: 0; bottom: 0;
    justify-content: center; font-size: 34px;
  }
  .card--back .wordmark {
    position: absolute; left: 96px; top: 54px; font-size: 28px;
  }

  .identity {
    position: absolute; left: 40px; top: 170px; width: 190px;
    text-align: right; color: var(--text-light);
  }
  .identity__name { font-weight: 700; font-size: 17px; }
  .identity__role { font-style: italic; font-size: 14px; color: var(--text-muted); margin-top: 2px; }
  .divider {
    position: absolute; left: 246px; top: 158px; width: 1px; height: 100px;
    background: var(--text-light);
  }
  .contact {
    position: absolute; left: 262px; top: 166px;
    list-style: none; color: var(--text-light); font-size: 13.5px; line-height: 21px;
  }
</style>
</head>
<body>
<main class="canvas">
  <section class="card card--back" aria-label="Business card, contact side">
    <span class="edge-tab edge-tab--blue"></span>
    <span class="edge-tab edge-tab--red"></span>
    <div class="wordmark"><span class="wordmark__dot"></span>Harwick Crest Partners</div>
    <div class="identity">
      <p class="identity__name">Daniel Marsh</p>
      <p class="identity__role">Project Manager</p>
    </div>
    <span class="divider"></span>
    <ul class="contact">
      <li>Tel: 000 000 0000</li>
      <li>Fax: 000 000 0000</li>
      <li>E-mail: daniel.marsh@hcp.example</li>
      <li>www.harwickcrestpartners.example</li>
    </ul>
  </section>

  <section class="card card--front" aria-label="Business card, logo side">
    <span class="edge-tab edge-tab--blue"></span>
    <span class="edge-tab edge-tab--red"></span>
    <div class="wordmark"><span class="wordmark__dot"></span>Harwick Crest Partners</div>
  </section>
</main>
</body>
</html>
```